Brivelle drinking water Label.

I want Drinking water label that stands out from the rest..Elegant Attractive and visible label design. Brand name is 'BRIVELLE'.

Target Market(s)

KENYA.

Industry/Entity Type

Water Company

Requirements
Must have
• Must be unique. Must be elegant and have vibrant and eye catching color.
Nice to have
• Clear or colored background with water like effects.
Should not have
• Should not have more that 4 colors.

```html
<!DOCTYPE html>
<html lang="en">
<head>
<meta charset="utf-8">
<title>Brivelle Drinking Water Label</title>
<link rel="stylesheet" href="https://fonts.googleapis.com/css2?family=Encode+Sans+Condensed:wght@400;500&display=swap">
<style>
  :root {
    --backdrop: #a8d3ec;
    --label-white: #f4f6f8;
    --brand-navy: #3d3f96;
    --aqua-text: #2e8fc9;
    --wave-light: #b9d8ef;
    --wave-deep: #4d55b4;
  }
  * { margin: 0; padding: 0; box-sizing: border-box; }
  html, body {
    width: 1187px;
    height: 1200px;
    overflow: hidden;
    background: var(--backdrop);
    font-family: "Encode Sans Condensed", "Arial Narrow", sans-serif;
  }
  .canvas {
    position: relative;
    width: 1187px;
    height: 1200px;
    display: flex;
    align-items: center;
    justify-content: center;
  }
  .label {
    position: relative;
    width: 560px;
    height: 820px;
    background: var(--label-white);
    display: flex;
    flex-direction: column;
    align-items: center;
    box-shadow: 0 10px 30px rgba(40, 90, 130, 0.15);
  }
  .tagline {
    margin-top: 40px;
    font-size: 22px;
    font-weight: 400;
    letter-spacing: 5px;
    color: var(--aqua-text);
    text-transform: uppercase;
  }
  .brand-name {
    margin-top: 150px;
    font-size: 150px;
    font-weight: 500;
    line-height: 1;
    color: var(--brand-navy);
    letter-spacing: 2px;
  }
  .brand-dot {
    margin-top: 90px;
    width: 40px;
    height: 40px;
    border-radius: 50%;
    background: var(--aqua-text);
  }
  .quantity {
    margin-top: 16px;
    text-align: center;
    color: var(--brand-navy);
  }
  .quantity-caption { font-size: 17px; font-weight: 400; }
  .quantity-value { font-size: 24px; font-weight: 400; margin-top: 4px; }
  .wave-band {
    position: absolute;
    left: 0;
    bottom: 0;
    width: 100%;
    height: 110px;
    background: linear-gradient(to bottom, var(--wave-light) 0%, #8fb4e4 45%, var(--wave-deep) 100%);
  }
</style>
</head>
<body>
  <main class="canvas">
    <section class="label">
      <p class="tagline">Water with added minerals</p>
      <h1 class="brand-name">Brivelle</h1>
      <div class="brand-dot"></div>
      <div class="quantity">
        <p class="quantity-caption">Net Quantity</p>
        <p class="quantity-value">500 ml.</p>
      </div>
      <div class="wave-band" role="img" aria-label="Layered blue water wave pattern along the bottom of the label"></div>
    </section>
  </main>
</body>
</html>
```